Velborne Systems needs a business card

The logo we have uploaded is going to be the image centered on the back.
The business card color is going to be black. Increase the contrast in the logo and lettering so the grey stands out from the black and is more readable. Keep the shadow effect if you can.
On the front, the only part of the logo that should be used is the Egyptian character. We would like the following information included: Name (first last), Title, Phone number, email and company name (Velborne Systems).
The images of colored sound waves we uploaded is a concept we would like implemented on the front as well but please do not use the exact image. It is for guideline purposes.
Get creative with the empty space. We are a technology company that deals with sound and lights. Please not too busy.
Thank you, we look forward to all your submissions.

```html
<!DOCTYPE html>
<html lang="en">
<head>
<meta charset="utf-8">
<title>Velborne Systems — Business Card</title>
<link href="https://fonts.googleapis.com/css2?family=Exo+2:wght@400;500;600&display=swap" rel="stylesheet">
<style>
  :root{
    --bg:#e9e7e4;
    --card-black:#2c2c2d;
    --accent-red:#e8323a;
    --steel-light:#bdbdbf;
    --steel-dark:#3a3a3c;
    --text-white:#ffffff;
    --brand-grey:#8a8a8c;
  }
  *{box-sizing:border-box;margin:0;padding:0}
  html,body{width:1200px;height:803px;overflow:hidden;background:var(--bg);font-family:"Exo 2",sans-serif}
  .stage{position:relative;width:1200px;height:803px}
  .card{position:absolute;width:600px;height:343px;background:var(--card-black);overflow:hidden;box-shadow:0 6px 18px rgba(0,0,0,.18)}
  .card-back{left:300px;top:38px}
  .card-front{left:300px;top:422px}
  .card-shapes{position:absolute;inset:0;width:100%;height:100%}
  .brand-name{position:absolute;display:flex;align-items:center;gap:12px;color:var(--brand-grey);font-weight:600;letter-spacing:1px;text-transform:uppercase}
  .brand-mark{width:14px;height:14px;background:var(--accent-red)}
  .card-back .brand-name{left:0;right:60px;top:0;bottom:0;justify-content:center;font-size:30px}
  .card-front .brand-name{left:40px;top:150px;font-size:22px}
  .back-website{position:absolute;right:22px;top:30px;writing-mode:vertical-rl;color:var(--text-white);font-size:12px;letter-spacing:1px}
  .contact-block{position:absolute;left:330px;top:70px;color:var(--text-white)}
  .person-name{font-size:24px;font-weight:500;letter-spacing:1px}
  .person-title{font-size:10px;letter-spacing:1px;margin-top:2px;text-transform:uppercase}
  .contact-list{list-style:none;margin-top:26px}
  .contact-list li{display:flex;align-items:flex-start;gap:10px;font-size:12px;line-height:1.25;margin-bottom:10px}
  .contact-icon{flex:none;width:18px;height:18px}
</style>
</head>
<body>
<main class="stage">

  <section class="card card-back" aria-label="Card back">
    <svg class="card-shapes" viewBox="0 0 600 343" aria-hidden="true">
      <defs>
        <linearGradient id="steelBack" x1="0" x2="1">
          <stop offset="0" stop-color="#4a4a4c"/>
          <stop offset=".5" stop-color="#c8c8ca"/>
          <stop offset="1" stop-color="#555557"/>
        </linearGradient>
      </defs>
      <path d="M548,0 H600 V343 H548 V40 Q548,0 548,0 Z" fill="url(#steelBack)"/>
      <path d="M540,0 Q548,30 548,60 V343 H540 V60 Q540,25 520,0 Z" fill="#1f1f20"/>
    </svg>
    <div class="brand-name"><span class="brand-mark"></span>Velborne Systems</div>
    <div class="back-website">www.velborne.io</div>
  </section>

  <section class="card card-front" aria-label="Card front">
    <svg class="card-shapes" viewBox="0 0 600 343" aria-hidden="true">
      <defs>
        <linearGradient id="steelFront" x1="0" x2="1" y1="0" y2="1">
          <stop offset="0" stop-color="#5a5a5c"/>
          <stop offset=".45" stop-color="#d0d0d2"/>
          <stop offset="1" stop-color="#4a4a4c"/>
        </linearGradient>
      </defs>
      <path d="M310,0 H600 V343 H430 L300,60 Q292,20 310,0 Z" fill="var(--accent-red)"/>
      <path d="M470,0 H600 V343 H572 V70 Q572,10 520,0 Z" fill="url(#steelFront)"/>
      <path d="M520,0 Q560,6 566,60 V343 H572 V70 Q572,10 530,0 Z" fill="#2a2a2b" opacity=".5"/>
    </svg>
    <div class="brand-name"><span class="brand-mark"></span>Velborne Systems</div>
    <div class="contact-block">
      <h1 class="person-name">DANA WHITLOW</h1>
      <p class="person-title">General Manager</p>
      <ul class="contact-list">
        <li>
          <svg class="contact-icon" viewBox="0 0 18 18" aria-hidden="true"><circle cx="9" cy="9" r="8" fill="none" stroke="#fff"/><path d="M6,5 l2,0 1,2 -1,1 q1,2 2,2 l1,-1 2,1 0,2 q-5,1 -7,-7z" fill="#fff"/></svg>
          014 275 3981
        </li>
        <li>
          <svg class="contact-icon" viewBox="0 0 18 18" aria-hidden="true"><circle cx="9" cy="9" r="8" fill="none" stroke="#fff"/><rect x="6.5" y="4.5" width="5" height="9" rx="1" fill="none" stroke="#fff"/></svg>
          014 275 3982
        </li>
        <li>
          <svg class="contact-icon" viewBox="0 0 18 18" aria-hidden="true"><circle cx="9" cy="9" r="8" fill="none" stroke="#fff"/><rect x="5" y="6" width="8" height="6" fill="none" stroke="#fff"/><path d="M5,6 l4,3 4,-3" fill="none" stroke="#fff"/></svg>
          dana@velborne.io
        </li>
        <li>
          <svg class="contact-icon" viewBox="0 0 18 18" aria-hidden="true"><circle cx="9" cy="9" r="8" fill="none" stroke="#fff"/><circle cx="9" cy="9" r="4.5" fill="none" stroke="#fff"/><path d="M4.5,9 h9 M9,4.5 v9" stroke="#fff"/></svg>
          www.velborne.io
        </li>
        <li>
          <svg class="contact-icon" viewBox="0 0 18 18" aria-hidden="true"><circle cx="9" cy="9" r="8" fill="none" stroke="#fff"/><path d="M9,14 q-4,-4 -4,-6.5 a4,4 0 0 1 8,0 q0,2.5 -4,6.5z" fill="none" stroke="#fff"/><circle cx="9" cy="7.5" r="1.3" fill="#fff"/></svg>
          <span>42 Harlow Lane, Unit 3,<br>East Wing</span>
        </li>
      </ul>
    </div>
  </section>

</main>
</body>
</html>
```